Brivora Collective Business Card Design

We need a business card design for Brivora Collective. We are a healthcare recruiting, wellness and education company. We partner with medical facilities to find quality candidates. We also offer free wellness courses.
The final design should communicate an emphasis on recruiting and wellness
The main purpose of the business card is to utilized it for networking events, give to hospitals, executives, VCs surgery centers and clinics. I want it to be sleek, clean, use of our brand colors and professional.

```html
<!DOCTYPE html>
<html lang="en">
<head>
<meta charset="utf-8">
<title>Brivora Collective Business Card</title>
<link rel="stylesheet" href="https://fonts.googleapis.com/css2?family=Montserrat:wght@400;500;700&display=swap">
<style>
  :root {
    --brand-green: #035c52;
    --card-white: #f3f3f3;
    --ink: #2c2c2c;
    --backdrop: #1c1c1c;
    --on-green: #f4f4f4;
  }
  * { box-sizing: border-box; margin: 0; padding: 0; }
  html, body {
    width: 1200px; height: 1059px; overflow: hidden;
    background: var(--backdrop);
    font-family: "Montserrat", sans-serif;
  }
  .canvas { position: relative; width: 1200px; height: 1059px; }
  .card {
    position: absolute; left: 256px; width: 690px; height: 392px;
    border-radius: 22px; overflow: hidden;
  }
  .card--front { top: 89px; background: var(--card-white); }
  .card--back { top: 547px; background: var(--brand-green); }

  .accent-bar {
    position: absolute; left: 0; top: 59px; width: 21px; height: 36px;
    background: var(--brand-green);
  }
  .person { position: absolute; left: 37px; top: 56px; }
  .person__name {
    font-weight: 700; font-size: 21px; letter-spacing: 0.5px;
    color: var(--brand-green); line-height: 1;
  }
  .person__title {
    font-weight: 400; font-size: 16px; color: var(--ink);
    margin-top: 5px; letter-spacing: 0.3px;
  }
  .address {
    position: absolute; left: 37px; top: 187px;
    font-size: 16px; line-height: 21px; color: var(--ink); letter-spacing: 0.3px;
  }
  .contacts { position: absolute; left: 37px; top: 250px; list-style: none; }
  .contacts li {
    display: flex; align-items: center; height: 25.3px;
    font-size: 16px; color: var(--ink); letter-spacing: 0.3px;
  }
  .contacts svg { width: 12px; height: 12px; margin-right: 9px; fill: var(--brand-green); }

  .brand-front {
    position: absolute; left: 356px; top: 0; width: 310px; height: 392px;
    display: flex; align-items: center; justify-content: center; gap: 14px;
  }
  .brand-front__square { width: 34px; height: 34px; background: var(--brand-green); border-radius: 6px; }
  .brand-front__name {
    font-weight: 500; font-size: 27px; line-height: 1.1; color: var(--brand-green);
  }

  .brand-back {
    position: absolute; left: 0; right: 0; top: 140px;
    display: flex; align-items: center; justify-content: center; gap: 18px;
  }
  .brand-back__square { width: 34px; height: 34px; background: var(--on-green); border-radius: 6px; }
  .brand-back__name {
    font-weight: 400; font-size: 44px; color: var(--on-green); letter-spacing: -0.5px;
  }
  .web-line {
    position: absolute; left: 0; right: 0; top: 340px; text-align: center;
    font-size: 15px; letter-spacing: 2px; color: var(--on-green);
  }
  .web-line strong { font-weight: 700; }
</style>
</head>
<body>
<main class="canvas">
  <section class="card card--front" aria-label="Card front">
    <div class="accent-bar"></div>
    <div class="person">
      <p class="person__name">DANIEL OSTRANDER</p>
      <p class="person__title">Owner &amp; Manager</p>
    </div>
    <p class="address">P.O. Box&nbsp; Street Name<br>Country Name AB, A5B 521</p>
    <ul class="contacts">
      <li><svg viewBox="0 0 12 12"><path d="M1 4c0-2 2-3 5-3s5 1 5 3v1H8V4H4v1H1z M2 6h8l1 5H1z"/></svg>555 204 8831</li>
      <li><svg viewBox="0 0 12 12"><path d="M3 0h6a1 1 0 0 1 1 1v10a1 1 0 0 1-1 1H3a1 1 0 0 1-1-1V1a1 1 0 0 1 1-1zm0 2v7h6V2z"/></svg>555-310-72614</li>
      <li><svg viewBox="0 0 12 12"><path d="M0 4l6-4 6 4v8H0z M1.5 5v5.5h9V5L6 8z"/></svg>info@brivoracollective.com</li>
      <li><svg viewBox="0 0 12 12"><path d="M6 0a6 6 0 1 1 0 12A6 6 0 0 1 6 0zm-2 2L2 4l2 2 1 3 2-1-1-3 2-1-1-2z"/></svg>www.brivoracollective.com</li>
    </ul>
    <div class="brand-front">
      <span class="brand-front__square"></span>
      <span class="brand-front__name">Brivora<br>Collective</span>
    </div>
  </section>

  <section class="card card--back" aria-label="Card back">
    <div class="brand-back">
      <span class="brand-back__square"></span>
      <span class="brand-back__name">Brivora Collective</span>
    </div>
    <p class="web-line">www.<strong>brivoracollective</strong>.com</p>
  </section>
</main>
</body>
</html>
```